Commercial Security Landing Page

We're looking for a simple customizable Bootstrap based single landing page similar to http://gridtemplex.net/preview/GT482K913

I have attached our Full Logo to incorporate into the design.
I can also attach other assets if required.

We're in the Commercial Security Industry, we specialize in (These must be included on the site):
- CCTV
- Access Control
- Automation
- Fire Monitoring
- Theft Protection/Burglar Alarms

More information:
We install these systems in customers businesses to protect them from theft, fire, etc. We do very high quality installs and only use the highest quality equipment for each customer. We do not do network security or anything like that, we focus completely in protecting businesses and homes through the use of CCTV, Access Control, Automation such as (light control, garage control, flood protection, etc), we also handle fire monitoring, theft protection, and burglar alarms.

Specs/Requirements:
- Must not be built with WordPress.
- Must be built using Twitter Bootstrap
- Any images used must not be copyright protected or contain royalties.
- Eye Catching Stock Photos or Placeholder so that we can replace with our own photos.
- SEO Friendly
- Easily adjustable
- Contains a contact form
- Customized to our industry.
- Must be "modern" and scalable across all devices.

Colors we like:
- #0C9ED9
- #595A5C
- #414142

Target Market(s)

Business Owners, Home Owners, Enterprise

Industry/Entity Type

Security Service

Coding

Coded - Design and coding required

Font styles to use
Sans Serif

Requirements
Must have
• Must contain highlights of the following bullet points:
• - CCTV
• - Access Control
• - Automation
• - Fire Monitoring
• - Theft Protection/Burglar Alarms
Nice to have
• - Twitter Bootstrap
• - Any images used must not be copyright protected or contain royalties.
• - Eye Catching Stock Photos or Placeholder so that we can replace with our own photos.
• - SEO Friendly
• Partner Section (Showing off our partners):
• Vexlo.net (https://www.vexlo.net/)
• Tarnel Gate (http://www.tarnelgate.net/)
• BQM (http://www.brenwickquillmoor.net/)
Should not have
• Should not be built on Wordpress

```html
<!DOCTYPE html>
<html lang="en">
<head>
<meta charset="utf-8">
<title>Kovalis – Commercial Security</title>
<link rel="stylesheet" href="https://fonts.googleapis.com/css2?family=Open+Sans:wght@400;600;700&display=swap">
<style>
:root{
  --blue:#0C9ED9;
  --grey:#595A5C;
  --dark:#414142;
  --black:#000;
  --white:#fff;
  --frame:#7a7a7a;
}
*{box-sizing:border-box;margin:0;padding:0}
html,body{width:1200px;height:3690px;overflow:hidden}
body{font-family:"Open Sans",Arial,sans-serif;background:var(--white);color:var(--white)}
section,header,footer{position:relative;width:1200px;overflow:hidden}
.abs{position:absolute}

/* hero */
.hero{height:628px;background:#0b1b2e}
.hero-photo{position:absolute;inset:0;background:linear-gradient(120deg,#1d2f46 0%,#3b5878 40%,#6f8fb2 70%,#9fb8d2 100%)}
.nav{position:absolute;left:0;top:0;width:100%;height:75px;background:rgba(0,0,0,.55)}
.brand{position:absolute;left:125px;top:14px;font-size:40px;font-weight:600;color:var(--white);letter-spacing:1px;display:flex;align-items:center;gap:12px}
.brand-box{width:36px;height:36px;border:4px solid var(--blue);border-radius:6px}
.nav-links{position:absolute;top:29px;left:605px;display:flex;list-style:none;font-size:14px;font-weight:600}
.nav-links li{margin-right:28px}
.nav-links .active{color:var(--blue)}
.dropdown{position:absolute;left:760px;top:80px;width:275px;height:201px;background:rgba(0,0,0,.85);list-style:none;padding:12px 0 0 16px;font-size:13px;font-weight:600}
.dropdown li{height:40px;line-height:40px}
.hero-title{left:284px;top:231px;width:301px;height:55px;border:2px solid var(--white);font-size:34px;font-weight:600;text-align:center;line-height:50px;letter-spacing:1px}
.hero-text{left:160px;top:330px;width:518px;font-size:13px;line-height:18px;font-weight:600}
.hero-rule{left:160px;top:472px;width:518px;height:2px;background:rgba(255,255,255,.8)}
.hero-more{left:160px;width:518px;top:506px;text-align:center;font-size:17px;font-weight:600}

/* about */
.about{height:356px;background:var(--black)}
.about h2{position:absolute;left:206px;top:44px;font-size:40px;font-weight:400;color:var(--blue)}
.about p{position:absolute;left:206px;top:118px;width:470px;font-size:12px;line-height:16px;color:var(--grey)}
.hl{color:var(--blue)}
.about .more{position:absolute;left:206px;top:300px;font-size:17px;color:var(--blue);font-weight:600}
.about-brand{left:690px;top:120px;width:290px;text-align:center;font-size:66px;font-weight:600;color:var(--blue)}
.about-rule{left:130px;bottom:0;width:940px;height:2px;background:var(--frame)}

/* products */
.product{height:356px}
.product.dark{background:var(--black);color:var(--white)}
.product.light{background:var(--white);color:var(--dark)}
.photo{position:absolute;top:28px;width:256px;height:301px;border:5px solid var(--frame)}
.arrow{position:absolute;top:166px;width:34px;height:36px;background:var(--blue);border-radius:3px;display:flex;align-items:center;justify-content:center}
.product h3{position:absolute;font-size:40px;font-weight:400;line-height:46px}
.product .rule{position:absolute;height:3px;background:var(--blue)}
.product p{position:absolute;width:380px;font-size:11px;line-height:14px;font-weight:600}
.product.light p{font-weight:400;color:var(--dark)}
.btn{position:absolute;width:121px;height:37px;background:var(--blue);color:var(--white);border-radius:3px;font-size:17px;font-weight:600;text-align:center;line-height:37px}
.dark h3{right:230px;text-align:right;top:48px}
.dark .rule{right:230px;top:100px;width:182px}
.dark p{right:232px;top:116px;text-align:right}
.dark .btn{right:231px;top:284px}
.dark h3.two-line{font-size:28px;line-height:32px;top:52px}
.dark .rule.two-line{top:124px}
.dark p.two-line{top:136px}
.light h3{left:208px;top:46px}
.light .rule{left:208px;top:100px;width:350px}
.light p{left:208px;top:116px}
.light .btn{left:208px;top:284px}

/* partners */
.partners{height:163px;background:var(--white);display:flex;align-items:center;justify-content:center;gap:150px;color:var(--dark);font-size:32px;font-weight:700}

/* service request */
.request{height:500px;background:var(--black);text-align:center}
.request h2{position:absolute;top:22px;width:100%;font-size:32px;font-weight:600}
.request .sub{position:absolute;top:68px;width:100%;font-size:10px;line-height:12px}
.form{position:absolute;left:512px;top:98px;width:241px}
.form .top{height:3px;background:var(--blue);margin-bottom:14px}
.field{height:56px;border-bottom:2px solid var(--blue);margin-bottom:4px;padding-top:10px}
.field label{display:block;font-size:17px;line-height:22px}
.field span{display:block;font-size:10px;line-height:14px;color:#ccc}
.field.msg{height:100px}
.field.msg span{font-size:17px;line-height:22px;color:var(--white)}
.submit{position:absolute;left:508px;top:407px;width:184px;height:36px;border:2px solid var(--blue);font-size:24px;font-weight:600;line-height:32px;text-align:center}

/* footer */
.footer{height:271px;background:var(--white);color:var(--dark)}
.foot-brand{left:150px;top:110px;width:180px;text-align:center;font-size:40px;font-weight:600;color:var(--blue)}
.foot-nav{left:389px;top:72px;list-style:none;font-size:13px;line-height:25px}
.contact{left:565px;top:72px;font-size:14px;line-height:19px;color:var(--grey)}
.contact div{display:flex;gap:8px;margin-bottom:14px}
.map{left:828px;top:65px;width:211px;height:151px;background:linear-gradient(135deg,#e9ecef,#d7dde3 60%,#cfe3c6)}
</style>
</head>
<body>

<header class="hero">
  <div class="hero-photo" role="img" aria-label="Office tower glass facade with a dome security camera in the foreground"></div>
  <nav class="nav">
    <div class="brand"><span class="brand-box"></span>Kovalis</div>
    <ul class="nav-links">
      <li>HOME</li><li>ABOUT US</li><li class="active">PRODUCTS</li><li>PARTNERS</li><li>CONTACT US</li>
    </ul>
  </nav>
  <ul class="dropdown">
    <li>CCTV</li><li>ACCESS CONTROL</li><li>AUTOMATION</li><li>FIRE MONITORING</li><li>THEFT PROTECTION/BURGLAR ALARMS</li>
  </ul>
  <div class="abs hero-title">SECURED</div>
  <p class="abs hero-text">Lorem ipsum dolor sit amet, consectetur adipiscing elit. Morbi auctor ipsum quis mauris tristique consectetur. Praesent vulputate vel lacus eget pretium. Lorem ipsum dolor sit amet, consectetur adipiscing elit. Praesent finibus porta nisi, sed scelerisque quam sodales nec. Sed sagittis, ex et dapibus lobortis, dui erat pretium massa, a cursus ipsum libero at eros. Nullam lectus ex, rutrum in tellus eget, viverra tristique leo. Class aptent taciti sociosqu ad litora torquent per conubia nostra, per inceptos himenaeos.</p>
  <div class="abs hero-rule"></div>
  <div class="abs hero-more">Read More</div>
</header>

<section class="about">
  <h2>ABOUT US</h2>
  <p>Lorem ipsum dolor sit amet, consectetur adipiscing elit. Morbi auctor ipsum quis mauris tristique consectetur. Praesent vulputate vel lacus eget pretium. Lorem ipsum dolor sit amet, consectetur adipiscing elit. <span class="hl">Praesent finibus porta nisi, sed scelerisque quam sodales nec. Sed sagittis, ex et dapibus lobortis, dui erat pretium massa, a cursus ipsum libero at eros.</span> Nullam lectus ex, rutrum in tellus eget, viverra tristique leo. Class aptent taciti sociosqu ad litora torquent per conubia nostra, per inceptos himenaeos.</p>
  <div class="more">Read More</div>
  <div class="abs about-brand">Kovalis</div>
  <div class="abs about-rule"></div>
</section>

<section class="product dark">
  <div class="photo" style="left:221px;background:linear-gradient(160deg,#f2f2f2,#bdbdbd 60%,#6d6d6d)" role="img" aria-label="White dome CCTV camera"></div>
  <div class="arrow" style="left:160px"><svg width="14" height="18" viewBox="0 0 14 18"><path d="M10 2 3 9l7 7" fill="none" stroke="#fff" stroke-width="3"/></svg></div>
  <div class="arrow" style="left:500px"><svg width="14" height="18" viewBox="0 0 14 18"><path d="m4 2 7 7-7 7" fill="none" stroke="#fff" stroke-width="3"/></svg></div>
  <h3>CCTV</h3><div class="rule"></div>
  <p>Lorem ipsum dolor sit amet, consectetur adipiscing elit. Morbi auctor ipsum quis mauris tristique consectetur. Praesent vulputate vel lacus eget pretium. Lorem ipsum dolor sit amet, consectetur adipiscing elit. <span class="hl">Praesent finibus porta nisi, sed scelerisque quam sodales nec. Sed sagittis, ex et dapibus lobortis, dui erat pretium massa, a cursus ipsum libero at eros.</span> Nullam lectus ex, rutrum in tellus eget, viverra tristique leo. Class aptent taciti sociosqu ad litora torquent per conubia nostra, per inceptos himenaeos.</p>
  <div class="btn">Read More</div>
</section>

<section class="product light">
  <h3>ACCESS CONTROL</h3><div class="rule"></div>
  <p>Lorem ipsum dolor sit amet, consectetur adipiscing elit. Morbi auctor ipsum quis mauris tristique consectetur. Praesent vulputate vel lacus eget pretium. Lorem ipsum dolor sit amet, consectetur adipiscing elit. <span class="hl">Praesent finibus porta nisi, sed scelerisque quam sodales nec. Sed sagittis, ex et dapibus lobortis, dui erat pretium massa, a cursus ipsum libero at eros.</span> Nullam lectus ex, rutrum in tellus eget, viverra tristique leo. Class aptent taciti sociosqu ad litora torquent per conubia nostra, per inceptos himenaeos.</p>
  <div class="btn">Read More</div>
  <div class="photo" style="left:723px;background:linear-gradient(160deg,#cfcfc4,#8b8b7e 55%,#3d3d36)" role="img" aria-label="Fingerprint and keypad access reader on a wall"></div>
  <div class="arrow" style="left:665px"><svg width="14" height="18" viewBox="0 0 14 18"><path d="M10 2 3 9l7 7" fill="none" stroke="#fff" stroke-width="3"/></svg></div>
  <div class="arrow" style="left:1005px"><svg width="14" height="18" viewBox="0 0 14 18"><path d="m4 2 7 7-7 7" fill="none" stroke="#fff" stroke-width="3"/></svg></div>
</section>

<section class="product dark">
  <div class="photo" style="left:221px;background:linear-gradient(170deg,#3e4e66,#8a9bb2 45%,#e9edf2 70%,#c9b6a2)" role="img" aria-label="Hand holding a smartphone showing a home automation app"></div>
  <div class="arrow" style="left:160px"><svg width="14" height="18" viewBox="0 0 14 18"><path d="M10 2 3 9l7 7" fill="none" stroke="#fff" stroke-width="3"/></svg></div>
  <div class="arrow" style="left:500px"><svg width="14" height="18" viewBox="0 0 14 18"><path d="m4 2 7 7-7 7" fill="none" stroke="#fff" stroke-width="3"/></svg></div>
  <h3>AUTOMATION</h3><div class="rule"></div>
  <p>Lorem ipsum dolor sit amet, consectetur adipiscing elit. Morbi auctor ipsum quis mauris tristique consectetur. Praesent vulputate vel lacus eget pretium. Lorem ipsum dolor sit amet, consectetur adipiscing elit. <span class="hl">Praesent finibus porta nisi, sed scelerisque quam sodales nec. Sed sagittis, ex et dapibus lobortis, dui erat pretium massa, a cursus ipsum libero at eros.</span> Nullam lectus ex, rutrum in tellus eget, viverra tristique leo. Class aptent taciti sociosqu ad litora torquent per conubia nostra, per inceptos himenaeos.</p>
  <div class="btn">Read More</div>
</section>

<section class="product light">
  <h3>FIRE MONITORING</h3><div class="rule"></div>
  <p>Lorem ipsum dolor sit amet, consectetur adipiscing elit. Morbi auctor ipsum quis mauris tristique consectetur. Praesent vulputate vel lacus eget pretium. Lorem ipsum dolor sit amet, consectetur adipiscing elit. <span class="hl">Praesent finibus porta nisi, sed scelerisque quam sodales nec. Sed sagittis, ex et dapibus lobortis, dui erat pretium massa, a cursus ipsum libero at eros.</span> Nullam lectus ex, rutrum in tellus eget, viverra tristique leo. Class aptent taciti sociosqu ad litora torquent per conubia nostra, per inceptos himenaeos.</p>
  <div class="btn">Read More</div>
  <div class="abs" style="left:665px;top:25px;width:407px;height:304px;background:radial-gradient(ellipse at 50% 45%,#e6e6e6 0%,#8a8a8a 35%,#111 70%)" role="img" aria-label="Ceiling smoke detector with rising smoke"></div>
</section>

<section class="product dark">
  <div class="photo" style="left:221px;background:linear-gradient(160deg,#f4f4f2,#d8d6d0 60%,#b8a892)" role="img" aria-label="Finger pressing an alarm keypad on a wall"></div>
  <div class="arrow" style="left:160px"><svg width="14" height="18" viewBox="0 0 14 18"><path d="M10 2 3 9l7 7" fill="none" stroke="#fff" stroke-width="3"/></svg></div>
  <div class="arrow" style="left:500px"><svg width="14" height="18" viewBox="0 0 14 18"><path d="m4 2 7 7-7 7" fill="none" stroke="#fff" stroke-width="3"/></svg></div>
  <h3 class="two-line">THEFT PROTECTION<br>BURGLAR ALARMS</h3><div class="rule two-line"></div>
  <p class="two-line">Lorem ipsum dolor sit amet, consectetur adipiscing elit. Morbi auctor ipsum quis mauris tristique consectetur. Praesent vulputate vel lacus eget pretium. Lorem ipsum dolor sit amet, consectetur adipiscing elit. <span class="hl">Praesent finibus porta nisi, sed scelerisque quam sodales nec. Sed sagittis, ex et dapibus lobortis, dui erat pretium massa, a cursus ipsum libero at eros.</span> Nullam lectus ex, rutrum in tellus eget, viverra tristique leo. Class aptent taciti sociosqu ad litora torquent per conubia nostra, per inceptos himenaeos.</p>
  <div class="btn">Read More</div>
</section>

<section class="partners">
  <span>BQM</span><span>Tarnel Gate</span><span>Vexlo.net</span>
</section>

<section class="request">
  <h2>SERVICE REQUEST</h2>
  <div class="sub">Tell us about your site and the systems you need protected.<br>Our team will reply within one business day.</div>
  <form class="form">
    <div class="top"></div>
    <div class="field"><label>Name:</label><span>insert your name</span></div>
    <div class="field"><label>Email:</label><span>insert your email address</span></div>
    <div class="field"><label>Subject:</label><span>insert your subject</span></div>
    <div class="field msg"><label>Message:</label><span>insert your message</span></div>
  </form>
  <div class="submit">Submit</div>
</section>

<footer class="footer">
  <div class="abs foot-brand">Kovalis</div>
  <ul class="abs foot-nav"><li>HOME</li><li>ABOUT US</li><li>PRODUCTS</li><li>PARTNERS</li><li>CONTACT US</li></ul>
  <div class="abs contact">
    <div><svg width="12" height="16" viewBox="0 0 12 16"><path d="M6 0a6 6 0 0 0-6 6c0 4 6 10 6 10s6-6 6-10a6 6 0 0 0-6-6zm0 8.5A2.5 2.5 0 1 1 6 3.5a2.5 2.5 0 0 1 0 5z" fill="#0C9ED9"/></svg><span>4th Street - Lorem Ipsum<br>Dolor Sit - 1111111</span></div>
    <div><svg width="14" height="14" viewBox="0 0 14 14"><path d="M3 0 5 4 3.5 5.5a8 8 0 0 0 5 5L10 9l4 2-1 3C6 14 0 8 0 1z" fill="#0C9ED9"/></svg><span>+123.456.789</span></div>
    <div><svg width="16" height="12" viewBox="0 0 16 12"><rect x="1" y="1" width="14" height="10" fill="none" stroke="#0C9ED9" stroke-width="1.6"/><path d="m1 1 7 6 7-6" fill="none" stroke="#0C9ED9" stroke-width="1.6"/></svg><span>yourmail@domain.com</span></div>
  </div>
  <div class="abs map" role="img" aria-label="Street map showing the office location"></div>
</footer>

</body>
</html>
```